Voxalindra Business card

we are a cloud data network and voice business communication's company - we target small and medium size business - please look into our website to learn more voxalindra.com
Target Market(s)
small business and mid size
Logo Text
VOXALINDRA
Logo styles of interest
Abstract Logo
Lettermark Logo
Requirements
Must have
- LOGO, SLOGAN ( linking every voice worldwide ) name title email, fax, our colors are grey white back and blue - on the back we want to have 4 icon logos a phone, a cloud , data, network

```html
<!DOCTYPE html>
<html lang="en">
<head>
<meta charset="utf-8">
<title>Voxalindra Business Card</title>
<link rel="stylesheet" href="https://fonts.googleapis.com/css2?family=Arimo:wght@400;700&family=Roboto+Condensed:wght@700&display=swap">
<style>
  :root {
    --paper: #ffffff;
    --ink: #1d1d1b;
    --accent: #6b9f86;
    --frame: #3a3a3a;
    --placeholder: #2a2a2a;
  }
  * { box-sizing: border-box; margin: 0; padding: 0; }
  html, body {
    width: 1200px; height: 256px; overflow: hidden;
    background: var(--paper);
  }
  body { position: relative; font-family: "Arimo", Arial, sans-serif; color: var(--ink); }

  .card {
    position: absolute; top: 5px; height: 238px;
    border: 1px solid var(--frame); background: var(--paper);
  }
  .card--front { left: 8px; width: 411px; }
  .card--back { left: 491px; width: 696px; }

  .holder { position: absolute; left: 19px; top: 22px; font-size: 14px; font-weight: 700; letter-spacing: -0.2px; white-space: nowrap; }
  .holder__title { color: var(--accent); font-weight: 700; }

  .contact { position: absolute; left: 248px; font-size: 11px; font-weight: 700; line-height: 15px; white-space: nowrap; }
  .contact--phones { top: 57px; }
  .contact--web { top: 115px; }
  .contact .accent { color: var(--accent); }

  .brand { position: absolute; left: 0; bottom: 0; width: 300px; height: 60px; }
  .brand__slogan {
    position: absolute; left: 83px; top: 2px;
    font-size: 10.5px; font-weight: 700; white-space: nowrap;
  }
  .brand__name {
    position: absolute; left: 4px; top: 16px;
    font-family: "Roboto Condensed", "Arial Narrow", sans-serif;
    font-weight: 700; font-size: 42px; line-height: 42px; letter-spacing: 0.5px;
    color: var(--ink); white-space: nowrap;
  }

  .service-icon { position: absolute; left: 340px; width: 40px; height: 36px; }
  .service-icon--phone { top: 6px; }
  .service-icon--globe { top: 68px; }
  .service-icon--network { top: 136px; height: 26px; width: 42px; left: 338px; }
  .service-icon--voice { top: 190px; width: 34px; height: 34px; left: 343px; }
  .placeholder { background: var(--placeholder); border-radius: 4px; }
</style>
</head>
<body>

<section class="card card--front">
  <p class="holder">Dana Whitlock <span class="holder__title">Sale Associate</span></p>

  <div class="contact contact--phones">
    <p>Cell (555) 214-7390</p>
    <p>Office (555) 318-4400</p>
  </div>

  <div class="contact contact--web">
    <p>Dwhitlock<span class="accent">@voxalindra.com</span></p>
    <p>Fax <span class="accent">(555) 214-7012</span></p>
  </div>

  <div class="brand">
    <p class="brand__slogan">linking every voice worldwide</p>
    <p class="brand__name">VOXALINDRA</p>
  </div>
</section>

<section class="card card--back">
  <div class="brand">
    <p class="brand__slogan">linking every voice worldwide</p>
    <p class="brand__name">VOXALINDRA</p>
  </div>

  <svg class="service-icon service-icon--phone" viewBox="0 0 40 36" aria-label="Phone service">
    <path d="M8 4 h7 l2 8 -4 3 q3 7 8 10 l3 -4 8 3 v7 q-2 3 -6 3 q-14 -2 -21 -20 q0 -7 3 -10 z"
          fill="var(--ink)"/>
    <path d="M22 6 q9 1 11 10" fill="none" stroke="var(--ink)" stroke-width="2"/>
  </svg>

  <svg class="service-icon service-icon--globe" viewBox="0 0 40 36" aria-label="Global network">
    <circle cx="20" cy="18" r="16" fill="none" stroke="var(--ink)" stroke-width="2"/>
    <ellipse cx="20" cy="18" rx="7" ry="16" fill="none" stroke="var(--ink)" stroke-width="1.5"/>
    <line x1="4" y1="18" x2="36" y2="18" stroke="var(--ink)" stroke-width="1.5"/>
    <line x1="20" y1="2" x2="20" y2="34" stroke="var(--ink)" stroke-width="1.5"/>
  </svg>

  <div class="service-icon service-icon--network placeholder" role="img"
       aria-label="World map with connected data points"></div>

  <div class="service-icon service-icon--voice placeholder" role="img"
       aria-label="Speaking head silhouette for voice service"></div>
</section>

</body>
</html>
```